Real Estate Agent Business Card Needs a New Eye Catching Design

Looking for a designer that can revamp a current business card.
Looking for something with a lot more style.
Something that will catch the eye

Included in the file:
The old business card. (Old Business Card)
A new place holder image to be used as headshot. (Temp Headshot)
Homevane KT Logo (KT logo)
Fair Dwelling Access Logo (AC logo)

The working PSD file will need to be delivered with the individual layers separated and edible. (I'll being changing the new headshot later)
Any fonts used also need to be delivered.

Overall, the old business card has the elements but in a horrible state.
If you have any questions, please feel free to reach out.

Thank you

Glen

Target Market(s)

Individuals want to either sale or buy a home

Industry/Entity Type

Real Estate Agent

Design Requirements:
Headshot needs to be a head and shoulders and have a transparent background.

The American Flag should implemented into the design somehow.

Both the KT logo and AC logo need to be incorporated.

All information on the OLD Business Card should be included.

Requirements
Must have
• Transparent head shot set against the final background
• American Flag and/or colors-theme incorporated
• KT logo and AC logo incorporated

```html
<!DOCTYPE html>
<html lang="en">
<head>
<meta charset="utf-8">
<title>Bright Point Real Estate – Business Card</title>
<link href="https://fonts.googleapis.com/css2?family=Poppins:wght@300;400;600;800&family=Hind:wght@300;500&display=swap" rel="stylesheet">
<style>
  :root{
    --backdrop:#272727;
    --card:#ffffff;
    --navy:#26388c;
    --red:#d7262b;
    --coral:#e8785c;
    --haze:#c9cde8;
  }
  html,body{margin:0;padding:0;width:1200px;height:1200px;overflow:hidden;background:var(--backdrop);}
  .card{
    position:absolute;left:160px;top:353px;width:840px;height:480px;overflow:hidden;
    background:
      radial-gradient(ellipse 260px 200px at 0% 100%, var(--haze), transparent 70%),
      radial-gradient(ellipse 420px 260px at 100% 80%, #dfe2f3, transparent 70%),
      var(--card);
    font-family:"Hind",sans-serif;color:var(--navy);
  }
  .flag-art{
    position:absolute;left:364px;top:0;width:476px;height:240px;
    background:
      linear-gradient(160deg, transparent 0%, rgba(255,255,255,0) 60%, #fff 100%),
      linear-gradient(90deg, rgba(255,255,255,0) 0%, rgba(80,85,160,.75) 25%, rgba(80,85,160,.85) 48%, rgba(232,120,92,.7) 52%, rgba(140,100,170,.55) 80%, rgba(232,120,92,.6) 100%);
    -webkit-mask-image:linear-gradient(200deg,#000 40%,transparent 95%);
            mask-image:linear-gradient(200deg,#000 40%,transparent 95%);
  }
  .brand{position:absolute;left:46px;top:46px;margin:0;font-family:"Poppins",sans-serif;font-weight:800;color:var(--navy);line-height:1;}
  .brand-name{display:block;font-size:58px;letter-spacing:-2px;}
  .brand-line{display:block;font-size:27px;letter-spacing:4px;margin-top:8px;}
  .agent{position:absolute;right:536px;top:208px;text-align:right;font-family:"Poppins",sans-serif;}
  .agent-name{margin:0;font-size:24px;font-weight:800;letter-spacing:-.5px;line-height:1.1;}
  .agent-title{margin:2px 0 0;font-size:24px;font-weight:300;letter-spacing:2px;line-height:1.2;}
  .headshot{
    position:absolute;left:24px;top:272px;width:212px;height:208px;
    background:radial-gradient(ellipse 70px 80px at 55% 35%, #b9bddd, transparent 75%),
               linear-gradient(180deg, transparent 45%, #3a3f86 75%, #2b2f6e 100%);
    border-radius:100px 100px 0 0;
  }
  .contact{position:absolute;left:342px;top:214px;margin:0;font-size:26px;font-weight:300;line-height:37.2px;}
  .contact b{font-family:"Hind",sans-serif;font-weight:500;}
  .contact .email{font-family:"Poppins",sans-serif;font-weight:600;font-size:21px;}
  .badges{position:absolute;left:598px;top:370px;display:flex;gap:22px;align-items:center;}
  .badge{display:flex;align-items:center;gap:6px;font-family:"Poppins",sans-serif;font-weight:600;font-size:10px;color:var(--navy);line-height:1.1;}
  .badge .mark{width:30px;height:30px;background:var(--navy);flex:none;}
  .accent-band{position:absolute;left:236px;bottom:0;width:604px;height:22px;
    background:linear-gradient(90deg, rgba(255,255,255,0), #f6c6b3 40%, var(--coral) 85%, #c8524a);}
</style>
</head>
<body>
  <section class="card">
    <div class="flag-art" role="img" aria-label="Waving American flag illustration with stars and stripes"></div>

    <h1 class="brand">
      <span class="brand-name">Bright Point</span>
      <span class="brand-line">REAL ESTATE</span>
    </h1>

    <div class="agent">
      <p class="agent-name">Dana Morrow</p>
      <p class="agent-title">Homevane</p>
    </div>

    <div class="headshot" role="img" aria-label="Head and shoulders portrait of the agent"></div>

    <p class="contact">
      <b>Direct:</b> 555-204-7716<br>
      <span class="email">dmorrow.sales@brightpointhomes.com</span><br>
      2210 North Ridge Road<br>
      Calder, NV 89050<br>
      <b>Office:</b> 555-318-4420<br>
      <b>Fax:</b> 555-318-4425
    </p>

    <div class="badges">
      <div class="badge"><span class="mark"></span><span>Fair Dwelling<br>Access</span></div>
      <div class="badge"><span class="mark"></span><span>Homevane<br>KT</span></div>
    </div>

    <div class="accent-band"></div>
  </section>
</body>
</html>
```